Wordpress Design Project for Bankruptcy Law Office in San Francisco

our current website: www.dorvanelilaw.example

we would like to re-design it for wordpress to make it faster and a bit more modern.

content should be similar to what we have there right now but also we do family law

please include logo for law office:

Law Office of Marta K. Dorvaneli

Thank you.
Updates

please see attached word document with logos that we like as an example.

we do tend to like color red.  darker red.

Please submit your design variations and logo as soon as possible.   We would like to go over them and make our decision

Reason: Please create couple of more variations of logo for your design, so we can make our decision what we like the most. Please see word doc for samples: Text: Law Office Of Marta K. Dorvaneli

Reason: final touches

Target Market(s)

bankruptcy and family law clients

Industry/Entity Type

Family Law

Requirements
Must have
• see examples of law sites
http://marketing.lexoriba.example/testimonials

- new logo: Law Office of Marta K. Dorvaneli
- client intake form
- blog
- contact us form

Nice to have
• - map
- red color
- on the front page a nice photo of SF or a happy family

```html
<!DOCTYPE html>
<html lang="en">
<head>
<meta charset="utf-8">
<title>Ledgerline 207 – Law Office of Marta K. Dorvaneli</title>
<link href="https://fonts.googleapis.com/css2?family=Open+Sans:ital,wght@0,400;0,600;0,700;1,400&family=Arimo:wght@700&display=swap" rel="stylesheet">
<style>
:root{
  --navy:#1b4a66;
  --teal:#2b6887;
  --teal-dark:#1d4d69;
  --btn:#0f3550;
  --gold:#c8a14a;
  --blue-text:#1f5f86;
  --hero-blue:#2a6b8f;
  --ink:#333;
  --soft:#f3f3f3;
  --footer:#e8e8e8;
}
*{box-sizing:border-box;margin:0;padding:0}
html,body{width:712px;height:1200px;overflow:hidden;background:#fff}
body{font-family:"Open Sans",sans-serif;color:var(--ink);position:relative}
.abs{position:absolute}
.topline{left:0;top:0;width:712px;height:3px;background:var(--navy)}
/* header */
.brand-mark{left:24px;top:22px;width:40px;height:40px;border-radius:50%;background:var(--navy)}
.brand-name{left:76px;top:22px;font-size:22px;font-weight:600;color:var(--navy);line-height:24px}
.brand-sub{left:76px;top:49px;font-size:13px;font-weight:600;color:var(--navy)}
.lang-label{left:548px;top:22px;font-size:8.5px;color:var(--blue-text)}
.lang-select{left:615px;top:18px;width:76px;height:17px;background:#dde7ee;font-size:8px;color:#2a4a60;padding:3px 5px}
.lang-select svg{position:absolute;right:6px;top:7px}
.call{left:516px;top:58px;font-size:10.5px;color:var(--blue-text)}
.call strong{font-size:16px;font-weight:400;color:#111;margin-left:4px}
/* nav */
.nav{left:0;top:88px;width:712px;height:30px;background:linear-gradient(#3a7ea2,#1f5575);display:flex;padding-left:14px}
.nav a{color:#fff;text-decoration:none;font-size:10px;line-height:30px;padding:0 16px;border-right:1px solid rgba(255,255,255,.25)}
.nav a.active{background:var(--gold)}
/* hero */
.hero{left:0;top:118px;width:712px;height:244px;background:#ebe5e7}
.hero-photo{left:0;top:118px;width:390px;height:244px;
  background:
    linear-gradient(90deg,rgba(235,229,231,0) 70%,#ebe5e7 100%),
    linear-gradient(160deg,#5d6166 0%,#9ea2a6 18%,#d8d6d6 34%,#f4f1f0 50%,#e6dcdc 68%,#d9b8b4 84%,#cfc6c6 100%)}
.hero-text{left:426px;top:190px;font-family:"Arimo",sans-serif;font-weight:700;color:var(--hero-blue);font-size:15.5px;line-height:22px}
.hero-text .big{font-size:27px;color:#245f80}
/* services */
.services{left:0;top:362px;width:712px;height:178px;background:var(--soft)}
.svc{position:absolute;top:378px;width:162px}
.svc h3{font-size:10.5px;font-weight:600;color:#111;margin-bottom:6px}
.svc .ph{height:66px;border:2px solid #fff;box-shadow:0 0 2px #aaa}
.svc h4{font-size:9px;font-weight:700;color:var(--blue-text);margin-top:6px}
.svc p{font-size:7.3px;line-height:11.5px;color:var(--blue-text)}
/* main */
.main{left:12px;top:554px;width:472px;font-size:7.4px;line-height:12.6px}
.main h2{font-size:10.5px;font-weight:600;color:#111;margin-bottom:6px}
.main p{margin-bottom:5px}
.main .sub{font-weight:700;color:#222;margin:4px 0 2px}
.rule{border-top:1px dotted #888;margin:10px 0 12px}
.story{display:flex;gap:10px;margin-top:8px}
.story .ph{flex:0 0 152px;height:100px}
.story h4{font-size:9px;font-weight:600;color:var(--blue-text);margin:2px 0 3px}
.story-tail{margin-top:7px}
/* sidebar */
.side{left:506px;top:540px;width:206px;height:610px;background:var(--teal)}
.side-head{position:absolute;left:0;width:206px;height:29px;background:var(--teal-dark);color:#fff;font-size:12px;font-variant:small-caps;padding:6px 12px;border-bottom:2px solid #3d7c9c}
.field-label{position:absolute;color:#fff;font-size:8.5px}
.field{position:absolute;width:180px;height:18px;background:#fff}
.copy{position:absolute;top:776px;color:#fff;font-size:7.5px;display:flex;align-items:center;gap:5px}
.copy span.box{width:8px;height:8px;background:#dde;display:inline-block}
.btn{position:absolute;top:794px;height:17px;background:var(--btn);color:#fff;font-size:8px;font-weight:700;text-align:center;line-height:17px}
.post-title{position:absolute;color:#fff;font-size:9px}
.post-text{position:absolute;width:185px;color:#fff;font-size:7.4px;font-style:italic;line-height:11.3px}
.more{position:absolute;color:#fff;font-size:7.8px;font-weight:700}
/* footer */
.footer{left:0;top:1150px;width:712px;height:50px;background:var(--footer);font-size:7.6px;color:#222}
.footer .l{position:absolute;left:14px;top:13px}
.footer .r{position:absolute;right:20px;top:13px}
</style>
</head>
<body>
<div class="abs topline"></div>

<header>
  <div class="abs brand-mark"></div>
  <div class="abs brand-name">LEDGERLINE207.com</div>
  <div class="abs brand-sub">Law Office of Marta K. Dorvaneli</div>
  <div class="abs lang-label">Select Language</div>
  <div class="abs lang-select">English
    <svg width="6" height="4" viewBox="0 0 6 4"><path d="M0 0h6L3 4z" fill="#2a4a60"/></svg>
  </div>
  <div class="abs call">CALL US NOW: <strong>(555) 014-2290</strong></div>
</header>

<nav class="abs nav">
  <a class="active" href="#">HOME</a><a href="#">ABOUT US</a><a href="#">AREAS OF PRACTISE</a><a href="#">RESOURCES</a><a href="#">BLOG</a><a href="#">FAQ</a><a href="#" style="border:0">CONTACT US</a>
</nav>

<section>
  <div class="abs hero"></div>
  <div class="abs hero-photo" role="img" aria-label="Photo of a calculator, glasses and overdue bills on a desk"></div>
  <div class="abs hero-text"><span class="big">Lorem Ipsum</span>&nbsp; is simply<br>dummy text of the printing and<br>typesetting industry.</div>
</section>

<section>
  <div class="abs services"></div>
  <div class="svc" style="left:16px"><h3>Debt Relief</h3><div class="ph" role="img" aria-label="Photo of a relaxed man lying in grass among papers" style="background:linear-gradient(#8aa65a,#6f8c3e)"></div><h4>Tittle goes here</h4><p>Lorem ipsum dolor sit amet, consectetur adipisicing elit, sed do eiusmod tempor incididunt ut labore et dolore magna</p></div>
  <div class="svc" style="left:193px"><h3>Fore Closure Prevention</h3><div class="ph" role="img" aria-label="Photo of a for sale sign by a white picket fence" style="background:linear-gradient(90deg,#ddd,#c63a32 40%,#b33 70%,#eee)"></div><h4>Tittle goes here</h4><p>Lorem ipsum dolor sit amet, consectetur adipisicing elit, sed do eiusmod tempor incididunt ut labore et dolore magna</p></div>
  <div class="svc" style="left:370px"><h3>Chapter 13</h3><div class="ph" role="img" aria-label="Photo of open law books on a table" style="background:linear-gradient(#5a3a22,#c9a98a 60%,#7a5638)"></div><h4>Tittle goes here</h4><p>Lorem ipsum dolor sit amet, consectetur adipisicing elit, sed do eiusmod tempor incididunt ut labore et dolore magna</p></div>
  <div class="svc" style="left:544px"><h3>Chapter 7</h3><div class="ph" role="img" aria-label="Photo of a row of leather-bound law books" style="background:linear-gradient(90deg,#3a2a1e,#8a5a34 50%,#4a3322)"></div><h4>Tittle goes here</h4><p>Lorem ipsum dolor sit amet, consectetur adipisicing elit, sed do eiusmod tempor incididunt ut labore et dolore magna</p></div>
</section>

<main class="abs main">
  <h2>WELCOME TO LEDGERLINE 207 - COMPLETE BANKRUPTCY INFORMATION</h2>
  <p>The Law Offices of Marta K. Dorvaneli is a consumer law office dedicated to consumer protection and zealously defending the rights of our clients.&nbsp; We offer the big firm quality legal representation with a small firm individualized attention to each client.</p>
  <p>Our office offers services in: all types of consumer bankruptcy filings, i.e. Chapter 7, Chapter 13, Chapter 11, negotiating a settlement of your debts, assisting you in the defense of collection litigation and defending you against foreclosure. Please review our site and see what we may be able to offer you. Feel free to call us at (555) 018-3372 or use our free case evaluation form.</p>
  <p class="sub">Speak to a Lawyer</p>
  <p>Unlike some other law firms, when you call the Law Office of Marta K. Dorvaneli you will speak to an actual attorney. Not a paralegal or assistant. And even after retaining our office you will still speak to an attorney unlike other firms where you cannot get a hold of your attorney after several attempts.</p>
  <p style="margin-top:8px">Lorem ipsum dolor sit amet, consectetuer adipiscing elit. Nam cursus. Morbi ut mi. Nullam enim leo, egestas id, condimentum at, laoreet mattis, massa. Sed eleifend nonummy diam. Praesent mauris ante, elementum et, bibendum at, posuere sit amet, nibh. Duis tincidunt lectus quis dui viverra vestibulum. Suspendisse vulputate aliquam dui. Nulla elementum dui ut augue. Aliquam vehicula mi at mauris. Maecenas placerat, nisl at consequat rhoncus, sem nunc gravida justo, quis eleifend arcu velit quis lacus. Morbi magna magna, tincidunt a, mattis non, imperdiet vitae</p>
  <div class="rule"></div>
  <h2>STORIES &amp; MORE INFORMATION</h2>
  <div class="story">
    <div class="ph" role="img" aria-label="Photo of a wooden judge's gavel beside a book" style="background:linear-gradient(135deg,#2a140c,#8a4a22 55%,#3a1e10)"></div>
    <div><h4>Story Tittle line goes here</h4>
      <p>Lorem ipsum dolor sit amet, consectetuer adipiscing elit. Nam cursus. Morbi ut mi. Nullam enim leo, egestas id, condimentum at, laoreet mattis, massa.</p>
      <p>Sed eleifend nonummy diam. Praesent mauris ante, elementum et, bibendum at, posuere sit amet, nibh. Duis tincidunt lectus quis dui viverra vestibulum. Suspendisse vulputate aliquam dui. Nulla elementum dui ut augue. Aliquam vehicula mi at mauris. Maecenas placerat, nisl at consequat rhoncus, sem nunc gravida justo, quis eleifend arcu velit quis lacus. Morbi magna magna, tincidunt a, mattis non, imperdiet vitae, tellus.</p></div>
  </div>
  <p class="story-tail">Mauris vel lacus vitae felis vestibulum volutpat. Etiam est nunc, venenatis in, tristique eu, imperdiet ac, nisl. Cum sociis natoque penatibus et magnis dis parturient montes, nascetur ridiculus mus. In iaculis facilisis massa.</p>
  <div class="story" style="margin-top:18px">
    <div class="ph" role="img" aria-label="Photo of a happy family with children on bicycles in a park" style="background:linear-gradient(#9cb86a,#b8403a 55%,#7a9a4a)"></div>
    <div><h4>Story Tittle line goes here</h4>
      <p>Lorem ipsum dolor sit amet, consectetuer adipiscing elit. Nam cursus. Morbi ut mi. Nullam enim leo, egestas id, condimentum at, laoreet mattis, massa.</p>
      <p>Sed eleifend nonummy diam. Praesent mauris ante, elementum et, bibendum at, posuere sit amet, nibh. Duis tincidunt lectus quis dui viverra vestibulum. Suspendisse vulputate aliquam dui. Nulla elementum dui ut augue. Aliquam vehicula mi at mauris. Maecenas placerat, nisl at consequat rhoncus, sem nunc gravida justo, quis eleifend arcu velit quis lacus. Morbi magna magna, tincidunt a, mattis non, imperdiet vitae, tellus.</p></div>
  </div>
  <p class="story-tail">Mauris vel lacus vitae felis vestibulum volutpat. Etiam est nunc, venenatis in, tristique eu, imperdiet ac, nisl. Cum sociis natoque penatibus et magnis dis parturient montes, nascetur ridiculus mus. In iaculis facilisis massa.</p>
</main>

<aside class="abs side"></aside>
<aside>
  <div class="side-head" style="left:506px;top:540px">Contact Form</div>
  <div class="field-label" style="left:518px;top:576px">Name:</div><div class="field" style="left:518px;top:587px"></div>
  <div class="field-label" style="left:518px;top:610px">Email:</div><div class="field" style="left:518px;top:621px"></div>
  <div class="field-label" style="left:518px;top:644px">Phone:</div><div class="field" style="left:518px;top:655px"></div>
  <div class="field-label" style="left:518px;top:677px">Subject:</div><div class="field" style="left:518px;top:689px"></div>
  <div class="field-label" style="left:518px;top:711px">Message:</div><div class="field" style="left:518px;top:723px;height:47px"></div>
  <div class="copy" style="left:519px"><span class="box"></span>Send a copy of this message to yourself</div>
  <div class="btn" style="left:518px;width:40px">SEND</div>
  <div class="btn" style="left:568px;width:42px">RESET</div>

  <div class="side-head" style="left:506px;top:826px;height:28px">Recent Blog &amp; News</div>
  <div class="post-title" style="left:519px;top:867px">Title line here</div>
  <div class="post-text" style="left:519px;top:881px">Lorem ipsum dolor sit amet, consectetuer adipiscing elit. Nam cursus. Morbi ut mi. Nullam enim leo, egestas id, condimentum at, laoreet mattis, massa.</div>
  <div class="more" style="left:519px;top:919px">LEARN MORE</div>
  <div class="more" style="left:519px;top:991px">LEARN MORE</div>
  <div class="post-title" style="left:519px;top:1015px">Title line here</div>
  <div class="post-text" style="left:519px;top:1028px">Proin dui lectus, cursus eu, mattis laoreet, viverra sit amet, quam. Curabitur vel dolor ultrices ipsum dictum tristique. Praesent vitae lacus. Ut velit enim, vestibulum non, fermentum nec, hendrerit quis, leo. Pellentesque rutrum malesuada neque.</div>
  <div class="more" style="left:519px;top:1090px">LEARN MORE</div>
</aside>

<footer class="abs footer">
  <div class="l">© 2012 Company Name &nbsp;|&nbsp; All right reserved &nbsp;|&nbsp; Term &amp; Conditions</div>
  <div class="r">HOME &nbsp;|&nbsp; ABOUT US &nbsp;|&nbsp; AREAS OF PRACTISE &nbsp;|&nbsp; RESOURCES &nbsp;|&nbsp; BLOG &nbsp;|&nbsp; FAQ &nbsp;|&nbsp; CONTACT US</div>
</footer>
</body>
</html>
```